I would like to design a flyer that I can put on car windows, inside peoples mailboxes. This flyer is to display Crestline Athletics and Wellness is now Open. I would like this to be a Free One Week Pass! I would like to have the following information on the flyer.
1) My logo - CRESTLINE ATHLETICS AND WELLNESS (I will upload the logo)
2) Hours of operation - Mon - Fri "5am - 10pm" Sat/Sun "6am -6pm"
3) Membership $59.00 "No Initiation Fee" Month to Month Membership.
Class are free. The Classes are Yoga, Salsa Classes, Bootcamps, HITT, Sports Performance,
4) Personal Training
5) Message Therapy
6) Address: 2871 Havelmoor Commerce Dr. Suite 213
Chantilly, VA 20347
7) mail@crestlineaw-example.com
8) Free One Week Pass

```html
<!DOCTYPE html>
<html lang="en">
<head>
<meta charset="UTF-8">
<title>Crestline Athletics and Wellness – Now Open</title>
<link rel="stylesheet" href="https://fonts.googleapis.com/css2?family=Oswald:wght@300;400;500&family=Roboto+Condensed:wght@400;700&family=Montserrat:wght@500&display=swap">
<style>
  :root {
    --ink: #0a0514;
    --red: #e8202a;
    --white: #ffffff;
    --silver: #b9b9c4;
  }
  * { margin: 0; padding: 0; box-sizing: border-box; }
  html, body { width: 970px; height: 1200px; overflow: hidden; background: var(--ink); }
  .flyer { position: relative; width: 970px; height: 1200px; background: var(--ink); overflow: hidden; color: var(--white); font-family: "Oswald", sans-serif; font-weight: 300; }
  .abs { position: absolute; }
  .frame-art { position: absolute; left: 0; top: 0; }

  .brand { position: absolute; left: 282px; top: 35px; display: flex; align-items: center; gap: 16px; }
  .brand-mark { width: 110px; height: 110px; border-radius: 50%; background: var(--red); }
  .brand-name { font-family: "Montserrat", sans-serif; font-weight: 500; color: var(--red); line-height: 1; }
  .brand-name .line1 { display: block; font-size: 52px; letter-spacing: -1px; }
  .brand-name .line2 { display: block; font-size: 13px; letter-spacing: 3.2px; margin-top: 10px; }

  .headline { left: 65px; top: 530px; font-size: 62px; line-height: 1; letter-spacing: -1px; white-space: nowrap; }
  .headline .accent { color: var(--red); font-weight: 500; }
  .price { left: 65px; top: 628px; font-size: 40px; line-height: 1; }
  .price .amount { color: var(--red); font-weight: 500; }

  .perks { left: 65px; top: 680px; list-style: none; }
  .perks li, .classes li { position: relative; padding-left: 18px; font-size: 38px; line-height: 58.7px; white-space: nowrap; }
  .perks li::before, .classes li::before { content: ""; position: absolute; left: 0; top: 50%; width: 6px; height: 6px; background: var(--red); }

  .divider { left: 484px; top: 554px; width: 2px; height: 406px; background: linear-gradient(to bottom, transparent, var(--silver) 50%, transparent); }

  .classes-tab { left: 531px; top: 543px; width: 55px; height: 249px; background: var(--red); }
  .classes-tab span { position: absolute; left: 50%; top: 50%; transform: translate(-50%, -50%) rotate(-90deg); font-family: "Roboto Condensed", sans-serif; font-weight: 700; font-size: 32px; letter-spacing: 3px; white-space: nowrap; }
  .classes { left: 603px; top: 532px; list-style: none; }
  .classes li { font-size: 36px; line-height: 55.3px; }

  .contact-icon { left: 536px; }
  .address { left: 592px; top: 840px; font-size: 29px; line-height: 34px; letter-spacing: 0.5px; }
  .email { left: 592px; top: 925px; font-family: "Roboto Condensed", sans-serif; font-weight: 700; font-size: 25px; }

  .socials { left: 57px; top: 1030px; display: flex; align-items: center; font-family: "Roboto Condensed", sans-serif; white-space: nowrap; }
  .website { font-weight: 700; font-size: 24px; margin-right: 30px; }
  .social { display: flex; align-items: center; gap: 8px; font-size: 17px; margin-right: 26px; }
  .social-square { width: 24px; height: 24px; border: 2px solid var(--white); border-radius: 4px; }

  .hours { left: 0; top: 1132px; width: 970px; text-align: center; font-size: 34px; letter-spacing: 0.2px; white-space: nowrap; }
</style>
</head>
<body>
<main class="flyer">
  <svg class="frame-art" width="970" height="1200" viewBox="0 0 970 1200" aria-hidden="true">
    <path d="M0 0 H268 Q120 45 0 90 Z" fill="var(--red)"/>
    <path d="M0 90 Q120 45 268 0 L262 0 Q120 40 0 82 Z" fill="var(--silver)"/>
    <path d="M0 1123 Q485 1060 970 1123 V1200 H0 Z" fill="var(--red)"/>
    <path d="M0 1123 Q485 1060 970 1123" fill="none" stroke="var(--white)" stroke-width="3"/>

    <circle cx="217" cy="339" r="140" fill="#c06a3c" stroke="var(--white)" stroke-width="3"/>
    <circle cx="767" cy="339" r="138" fill="#9c8a80" stroke="var(--white)" stroke-width="3"/>
    <defs>
      <linearGradient id="sky" x1="0" y1="0" x2="0" y2="1">
        <stop offset="0" stop-color="#4d6c99"/>
        <stop offset="0.7" stop-color="#b7c4d4"/>
        <stop offset="1" stop-color="#7a6550"/>
      </linearGradient>
      <radialGradient id="dance" cx="0.5" cy="0.4" r="0.6">
        <stop offset="0" stop-color="#e49a5e"/>
        <stop offset="1" stop-color="#8a3b25"/>
      </radialGradient>
      <radialGradient id="gym" cx="0.5" cy="0.4" r="0.6">
        <stop offset="0" stop-color="#d9b49a"/>
        <stop offset="1" stop-color="#6f6a66"/>
      </radialGradient>
    </defs>
    <circle cx="217" cy="339" r="138" fill="url(#dance)" role="img" aria-label="Photo of a couple dancing salsa"/>
    <circle cx="767" cy="339" r="136" fill="url(#gym)" role="img" aria-label="Photo of two fit athletes holding a dumbbell"/>
    <circle cx="482" cy="336" r="172" fill="url(#sky)" stroke="var(--white)" stroke-width="3" role="img" aria-label="Photo of a woman in a yoga lunge pose on a beach at sunrise"/>
  </svg>

  <header class="brand">
    <div class="brand-mark"></div>
    <h1 class="brand-name"><span class="line1">CRESTLINE</span><span class="line2">ATHLETICS AND WELLNESS</span></h1>
  </header>

  <h2 class="abs headline">7 DAYS <span class="accent">FREE</span> TRIAL</h2>
  <p class="abs price">MEMBERSHIP: <span class="amount">$59.00</span></p>
  <ul class="abs perks">
    <li>No Initiation Fee</li>
    <li>Month to Month Membership</li>
    <li>Classes are FREE</li>
    <li>Personal Training</li>
    <li>Massage Therapy</li>
  </ul>

  <div class="abs divider"></div>

  <div class="abs classes-tab"><span>OUR CLASSES</span></div>
  <ul class="abs classes">
    <li>YOGA</li>
    <li>SALSA CLASSES</li>
    <li>BOOTCAMPS</li>
    <li>HITT</li>
    <li>SPORTS PERFORMANCE</li>
  </ul>

  <svg class="abs contact-icon" style="top:838px" width="24" height="40" viewBox="0 0 24 40" aria-hidden="true">
    <path d="M12 0 C5 0 0 5 0 12 C0 21 12 40 12 40 C12 40 24 21 24 12 C24 5 19 0 12 0 Z" fill="var(--red)"/>
    <circle cx="12" cy="12" r="5" fill="var(--ink)"/>
  </svg>
  <p class="abs address">2871 Havelmoor Commerce Dr.<br>Suite 213, Chantilly, VA 20347</p>

  <svg class="abs contact-icon" style="top:929px;left:534px" width="36" height="24" viewBox="0 0 36 24" aria-hidden="true">
    <rect x="0" y="0" width="36" height="24" rx="2" fill="var(--red)"/>
    <path d="M0 2 L18 14 L36 2" fill="none" stroke="var(--ink)" stroke-width="2.5"/>
  </svg>
  <p class="abs email">mail@crestlineaw-example.com</p>

  <div class="abs socials">
    <span class="website">www.crestlineaw-example.com</span>
    <span class="social"><span class="social-square"></span>CrestlineAthleticsAndWellness</span>
    <span class="social"><span class="social-square"></span>@crestlineathleticswellness</span>
  </div>

  <p class="abs hours">Hours of operation: Mon - Fri: 5am - 10pm;&nbsp; Sat/Sun: 6am -6pm</p>
</main>
</body>
</html>
```